Cover and label for Christian CD with lively original music for kids

The album title is Hope Runs Wide. It's for children, but is also designed to be enjoyable for older members of the family to listen to. The final cover should reflect the over-arching theme of God's love from a Christian perspective. If it depicts children, It should be culturally and racially inclusive. It should evoke feelings of warmth, joy and belonging (or at least openness) for viewers. And it should appeal to kids and adults. There should be some bright color but no overwhelmingly "loud" designs please. Album title and artist name should be clear-Hope Runs Wide and Miss Tilda respectively (may need flexibility on artist name as that has not been finalized). Label should be adapted from or complementary to cover art.

Industry/Entity Type

Christian

```html
<!DOCTYPE html>
<html lang="en">
<head>
<meta charset="utf-8">
<title>Hope Runs Wide — Miss Tilda</title>
<link rel="stylesheet" href="https://fonts.googleapis.com/css2?family=Montserrat:wght@400&family=Sniglet:wght@400;800&display=swap">
<style>
  :root {
    --backdrop: #f1f2f2;
    --teal-deep: #1fb2c6;
    --teal-mid: #3cc6d4;
    --teal-light: #8edde6;
    --cloud: #c9eef2;
    --title-white: #ffffff;
    --artist-grey: #3d5a60;
  }
  html, body {
    margin: 0;
    padding: 0;
    width: 1200px;
    height: 878px;
    overflow: hidden;
    background: var(--backdrop);
  }
  .canvas {
    position: relative;
    width: 1200px;
    height: 878px;
  }
  .album-cover {
    position: absolute;
    left: 280px;
    top: 119px;
    width: 640px;
    height: 640px;
    overflow: hidden;
    box-shadow: 0 6px 24px rgba(0, 0, 0, 0.12);
  }
  .sky-wash {
    position: absolute;
    inset: 0;
    background:
      radial-gradient(ellipse 40% 25% at 30% 78%, var(--cloud) 0%, transparent 70%),
      radial-gradient(ellipse 35% 22% at 72% 82%, var(--cloud) 0%, transparent 70%),
      radial-gradient(ellipse 45% 30% at 55% 30%, var(--teal-light) 0%, transparent 70%),
      radial-gradient(ellipse 30% 20% at 18% 20%, var(--teal-light) 0%, transparent 70%),
      linear-gradient(160deg, var(--teal-deep) 0%, var(--teal-mid) 55%, var(--teal-deep) 100%);
  }
  .artist-name {
    position: absolute;
    top: 30px;
    left: 0;
    right: 0;
    margin: 0;
    text-align: center;
    font-family: "Montserrat", sans-serif;
    font-weight: 400;
    font-size: 15px;
    letter-spacing: 1.6em;
    padding-left: 1.6em;
    color: var(--artist-grey);
  }
  .album-title {
    position: absolute;
    top: 190px;
    left: 0;
    right: 0;
    margin: 0;
    text-align: center;
    font-family: "Sniglet", cursive;
    font-weight: 400;
    color: var(--title-white);
    line-height: 0.95;
  }
  .album-title .title-main {
    display: block;
    font-size: 112px;
    letter-spacing: 0.02em;
  }
  .album-title .title-small {
    font-size: 52px;
    vertical-align: middle;
    margin-right: 10px;
  }
</style>
</head>
<body>
  <main class="canvas">
    <section class="album-cover">
      <div class="sky-wash" role="img" aria-label="Soft turquoise watercolor sky with pale drifting clouds"></div>
      <p class="artist-name">MISS TILDA</p>
      <h1 class="album-title">
        <span class="title-main">HOPE</span>
        <span class="title-main"><span class="title-small">runs</span>WIDE</span>
      </h1>
    </section>
  </main>
</body>
</html>
```